Business card and stationery for new company
Member of Verola Group
Business card and stationery for new company - Aviation
Creative Brief
Professional
Bayu Santoso Wiratmaja
Managing Director
Jalan Cemara Lestari III no 8 Sukamulya Tengah South Jakarta 12450
+62 21 57186324 (Ext 204)
bayu.wiratmaja@verola-group.example

```html
<!DOCTYPE html>
<html lang="en">
<head>
<meta charset="utf-8">
<title>Karya Tama Mandiri — Business Card</title>
<link rel="stylesheet" href="https://fonts.googleapis.com/css2?family=Arimo:wght@400;700&display=swap">
<style>
  :root {
    --backdrop: #2c2c2e;
    --card-white: #f7f7f9;
    --brand-purple: #3b2c8c;
    --accent-grey: #9a9aa6;
    --text-dark: #3b2c8c;
    --text-grey: #55555f;
    --card-w: 520px;
    --card-h: 297px;
  }
  * { box-sizing: border-box; margin: 0; padding: 0; }
  html, body {
    width: 1200px; height: 881px; overflow: hidden;
    background: var(--backdrop);
    font-family: "Arimo", Arial, sans-serif;
  }
  .stage {
    width: 1200px; height: 881px;
    display: flex; align-items: center; justify-content: center; gap: 60px;
  }
  .card {
    position: relative;
    width: var(--card-w); height: var(--card-h);
    border-radius: 4px; overflow: hidden;
    box-shadow: 0 10px 30px rgba(0,0,0,.45);
  }
  .card--front { background: var(--card-white); }
  .card--back  { background: var(--brand-purple); }

  .card__swoosh { position: absolute; inset: 0; width: 100%; height: 100%; }

  .company {
    position: absolute; display: flex; align-items: center; gap: 8px;
    color: var(--brand-purple); font-weight: 400; white-space: nowrap;
  }
  .company__mark { background: currentColor; flex: none; }
  .card--front .company { left: 30px; top: 118px; font-size: 18px; }
  .card--front .company__mark { width: 10px; height: 10px; }
  .card--back .company { left: 0; right: 0; top: 128px; justify-content: center; color: #ffffff; font-size: 30px; gap: 12px; }
  .card--back .company__mark { width: 16px; height: 16px; }

  .contact {
    position: absolute; left: 262px; top: 30px; width: 240px;
    color: var(--text-grey); font-size: 9px; line-height: 1.45;
  }
  .contact__name { color: var(--text-dark); font-size: 13px; font-weight: 700; }
  .contact__title { font-size: 9px; margin-bottom: 14px; }
  .contact__address { margin-bottom: 12px; }
  .contact__list { list-style: none; }
  .contact__list li { display: flex; align-items: center; gap: 6px; }
  .contact__icon { width: 8px; height: 8px; fill: var(--brand-purple); flex: none; }
</style>
</head>
<body>
<main class="stage">

  <section class="card card--front" aria-label="Business card front">
    <svg class="card__swoosh" viewBox="0 0 520 297" preserveAspectRatio="none" aria-hidden="true">
      <path d="M0 210 C 140 250, 300 250, 520 226 L520 232 C 300 258, 140 262, 0 226 Z" fill="var(--accent-grey)"/>
      <path d="M0 236 C 150 268, 320 262, 520 240 L520 297 L0 297 Z" fill="var(--brand-purple)"/>
    </svg>

    <p class="company"><span class="company__mark" aria-hidden="true"></span>Karya Tama Mandiri</p>

    <div class="contact">
      <p class="contact__name">Bayu Santoso Wiratmaja</p>
      <p class="contact__title">Managing Director</p>
      <p class="contact__address">Jalan Cemara Lestari III no 8<br>Sukamulya Tengah South Jakarta<br>12450</p>
      <ul class="contact__list">
        <li><svg class="contact__icon" viewBox="0 0 8 8"><rect width="8" height="8" rx="1"/></svg>+62 21 57186324 (Ext 204)</li>
        <li><svg class="contact__icon" viewBox="0 0 8 8"><rect width="8" height="8" rx="1"/></svg>+62 21 57186330</li>
        <li><svg class="contact__icon" viewBox="0 0 8 8"><rect width="8" height="8" rx="1"/></svg>+62 21 57186331</li>
        <li><svg class="contact__icon" viewBox="0 0 8 8"><rect width="8" height="8" rx="1"/></svg>bayu.wiratmaja@verola-group.example</li>
      </ul>
    </div>
  </section>

  <section class="card card--back" aria-label="Business card back">
    <p class="company"><span class="company__mark" aria-hidden="true"></span>Karya Tama Mandiri</p>
  </section>

</main>
</body>
</html>
```